BrivoMatex. Lantern for the Steady Growth. Business card

Professional business card for BrivoMatex (Lantern for the Steady Growth)
My rationale: Strategy-> Execution-> Results-> Value that lead to the BrivoMatex name: We put the Lantern for the Steady Growth.
We deliver value to our customers helping them at defining a good strategy (cyan arrow). 90% of well formulated strategies fail due to poor execution so we also consider strategical execution very important (green arrow). Due to the execution we obtain the results (blue arrow). Finally, the results provide feedback to redefine strategy, and the new strategy has to be executed and new results obtained providing new feedback and on and on. It's like a wheel that finally, must create corporate value: value for shareholders, staholders, employees, providers...-

Target Market(s)

CEOs and steering comitees , invewrnent funds

Industry/Entity Type

Business Consultant

Contact Information for Business Card

Tommaso Ferlini
CEO & Founder
tommaso.ferlini@brivomatex.example
Mobile: +34 611.205.938
www.brivomatex.example

Colors

Designer to choose colors to be used in the design.

Requirements
Nice to have
• Nice to hace the words: Strategy, execution, results
• Nice to vave the claim: Lantern for the Steady Growth
• The three colors should be shown:
• cyan for STRATEGY
• green for EXECUTION
• blue for RESULTS
Should not have
• Complete black background

```html
<!DOCTYPE html>
<html lang="en">
<head>
<meta charset="utf-8">
<title>BrivoMatex business card</title>
<link rel="stylesheet" href="https://fonts.googleapis.com/css2?family=Arimo:wght@400;700&display=swap">
<style>
  :root {
    --paper: #ffffff;
    --night: #000000;
    --frame: #cfcfcf;
    --strip: #9a9a9a;
    --accent: #e8130f;
    --ink: #6b6b6b;
    --ink-soft: #8c8c8c;
    --rule: #d6d6d6;
  }
  * { box-sizing: border-box; margin: 0; padding: 0; }
  html, body { width: 1200px; height: 1200px; overflow: hidden; background: var(--paper); }
  body { position: relative; font-family: "Arimo", Arial, sans-serif; color: var(--ink); }

  .night-band { position: absolute; left: 0; top: 557px; width: 1200px; height: 571px; background: var(--night); }
  .floor-strip { position: absolute; left: 0; top: 1128px; width: 1200px; height: 24px; background: var(--strip); }

  .card {
    position: absolute; left: 192px; width: 768px; height: 439px;
    background: var(--paper); border: 14px solid var(--frame); overflow: hidden;
  }
  .card--front { top: 53px; }
  .card--back { top: 619px; height: 432px; }

  .card__edge-band { position: absolute; right: 0; top: 0; width: 46px; height: 100%; background: var(--frame); }
  .card__edge-band::after { content: ""; position: absolute; left: 10px; top: 0; width: 28px; height: 100%; background: var(--accent); }

  .card__half-dot { position: absolute; left: -14px; top: 186px; width: 60px; height: 60px; border-radius: 50%; background: var(--accent); }

  .brand { position: absolute; left: 50px; top: 70px; width: 340px; text-align: center; }
  .brand__dot { display: block; width: 44px; height: 44px; margin: 0 auto 30px; border-radius: 50%; background: var(--accent); }
  .brand__name { font-size: 34px; font-weight: 700; color: var(--ink); letter-spacing: 0.5px; }
  .brand__claim { margin-top: 10px; font-size: 17px; color: var(--ink-soft); }

  .card__divider { position: absolute; left: 394px; top: 65px; width: 3px; height: 270px; background: var(--rule); }

  .person { position: absolute; left: 430px; top: 118px; width: 260px; }
  .person__name { font-size: 22px; font-weight: 700; color: var(--ink); }
  .person__role { margin-top: 22px; font-size: 17px; color: var(--ink-soft); }
  .person__email { margin-top: 24px; font-size: 13px; color: var(--ink-soft); white-space: nowrap; }

  .contact-line { position: absolute; left: 60px; top: 332px; width: 640px; text-align: center; font-size: 17px; color: var(--ink-soft); }
</style>
</head>
<body>
  <div class="night-band"></div>
  <div class="floor-strip"></div>

  <section class="card card--front">
    <span class="card__half-dot"></span>
    <div class="brand">
      <span class="brand__dot"></span>
      <div class="brand__name">BrivoMatex</div>
      <div class="brand__claim">Lantern for the Steady Growth</div>
    </div>
    <span class="card__divider"></span>
    <div class="person">
      <div class="person__name">Tommaso Ferlini</div>
      <div class="person__role">CEO &amp; Founder</div>
      <div class="person__email">tommaso.ferlini@brivomatex.example</div>
    </div>
    <div class="contact-line">Mobile: +34 611.205.938 &nbsp;·&nbsp; www.brivomatex.example</div>
    <span class="card__edge-band"></span>
  </section>

  <section class="card card--back">
    <span class="card__half-dot"></span>
    <div class="brand">
      <span class="brand__dot"></span>
      <div class="brand__name">BrivoMatex</div>
      <div class="brand__claim">Lantern for the Steady Growth</div>
    </div>
    <span class="card__divider"></span>
    <div class="person">
      <div class="person__name">Tommaso Ferlini</div>
      <div class="person__role">CEO &amp; Founder</div>
      <div class="person__email">tommaso.ferlini@brivomatex.example</div>
    </div>
    <div class="contact-line">Mobile: +34 611.205.938 &nbsp;·&nbsp; www.brivomatex.example</div>
    <span class="card__edge-band"></span>
  </section>
</body>
</html>
```